New business! Essential Oils Label for 10 mL Essential Oils Bottles

I need a label design for my new essential oils business. The design should be easily transferable between products. Content should include:
label size W x H 1.25 x 2.875

LAVENDER
Lavandula angustifolia
VOLMIRAâ„¢
100% PURE ESSENTIAL OIL
Net 10 mL
For promotions and additional product information visit fb.com/VolmiraOils
VolmiraOils.com
Coral Vista, FL 33871
888-555-KIPO (5476)
Indications: Massage (10 drops of carrier oil for every drop of essential oil), Bath (10 drops of essential oil) or Inhalation (2-4 drops essential of on a tissue).
EXTERNAL USE ONLY- DILUTE BEFORE APPLICATION
Caution: Do not ingest the oil. Sensitive skin may be irritated by topical use. Avoid contact with eyes. Consult your healthcare practitioner before use. Store oil away from children and pets. Not meant for use during pregnancy. Seek medical care immediately if adverse reaction is experienced.

Target Market(s)

ONLINE SHOPPERS

Industry/Entity Type

Business

Font styles to use
Serif
Sans Serif

Colors

Designer to choose colors to be used in the design.

Requirements
Must have
• CONTENT AS LISTED IN PROJECT DESCRIPTION, LOGO (ATTACHED)
Nice to have
• Files with easily transferable content so the same label design can be used for multiple products.
Should not have
• Too small of print, difficult to read

```html
<!DOCTYPE html>
<html lang="en">
<head>
<meta charset="utf-8">
<title>Volmira Lavender Essential Oil Label</title>
<link rel="stylesheet" href="https://fonts.googleapis.com/css2?family=Poppins:wght@300;500&family=Montserrat:wght@700;800&family=Open+Sans:wght@400;600&display=swap">
<style>
  :root {
    --page: #ececec;
    --label-light: #f6d89c;
    --label-deep: #e8b46a;
    --purple: #5a3a9b;
    --purple-line: #5b3ec0;
    --ink: #2a2118;
    --gold: #eab23c;
    --cream: #f6e6c6;
    --badge: #1c1a18;
  }
  html, body {
    margin: 0;
    padding: 0;
    width: 1114px;
    height: 1200px;
    overflow: hidden;
    background: var(--page);
  }
  .label {
    position: absolute;
    top: 320px;
    left: 20px;
    display: flex;
    gap: 12px;
  }
  .panel {
    position: relative;
    width: 350px;
    height: 560px;
    background: linear-gradient(180deg, var(--label-light) 0%, var(--label-deep) 100%);
    overflow: hidden;
  }
  .panel-frame {
    position: absolute;
    top: 40px;
    bottom: 40px;
    border: 3px solid var(--purple-line);
    border-radius: 18px;
  }
  .frame-open-left { left: -20px; right: 22px; }
  .frame-open-right { left: 22px; right: -20px; }
  .panel-content {
    position: absolute;
    width: 560px;
    height: 350px;
    left: -105px;
    top: 105px;
    transform: rotate(-90deg);
    box-sizing: border-box;
    display: flex;
    flex-direction: column;
    justify-content: center;
    color: var(--ink);
    font-family: "Open Sans", sans-serif;
  }
  .reads-down { transform: rotate(90deg); }

  /* Front panel */
  .front { align-items: center; gap: 12px; padding: 0 40px; }
  .brand-name {
    font-family: "Poppins", sans-serif;
    font-weight: 300;
    font-size: 72px;
    letter-spacing: 8px;
    line-height: 1;
    color: var(--ink);
  }
  .brand-name sup { font-size: 16px; letter-spacing: 0; vertical-align: top; }
  .product-box {
    width: 450px;
    height: 182px;
    background: var(--purple);
    border-radius: 14px;
    display: flex;
    flex-direction: column;
    align-items: center;
    justify-content: center;
    gap: 8px;
  }
  .product-name {
    font-family: "Poppins", sans-serif;
    font-weight: 500;
    font-size: 64px;
    letter-spacing: 4px;
    line-height: 1;
    color: var(--cream);
  }
  .latin-name {
    font-family: "Open Sans", sans-serif;
    font-size: 27px;
    color: var(--cream);
    border: 2px solid var(--cream);
    border-radius: 10px;
    padding: 0 12px;
    line-height: 1.25;
  }
  .purity {
    font-family: "Montserrat", sans-serif;
    font-weight: 800;
    font-size: 22px;
    color: var(--gold);
  }
  .net { font-size: 20px; color: var(--ink); }

  /* Distributor panel */
  .distributor { align-items: center; justify-content: center; gap: 34px; padding: 0 60px; }
  .contact { font-size: 17px; line-height: 1.45; }
  .contact .small { font-size: 12px; text-align: center; }
  .badge {
    background: var(--badge);
    border-radius: 8px;
    padding: 10px 14px;
    text-align: center;
    color: var(--cream);
  }
  .badge-name {
    font-family: "Poppins", sans-serif;
    font-weight: 300;
    font-size: 30px;
    letter-spacing: 3px;
    line-height: 1.1;
  }
  .badge-tag { font-family: "Montserrat", sans-serif; font-weight: 700; font-size: 9px; letter-spacing: 0.5px; }

  /* Directions panel */
  .directions { padding: 36px 60px; gap: 10px; font-size: 14.5px; line-height: 1.3; text-align: justify; }
  .directions p { margin: 0; }
  .warning { text-align: center; font-size: 15px; line-height: 1.25; margin-top: 8px; }
</style>
</head>
<body>
  <div class="label">
    <section class="panel">
      <div class="panel-frame frame-open-left"></div>
      <div class="panel-content distributor reads-down">
        <div class="badge">
          <div class="badge-name">VOLMIRA</div>
          <div class="badge-tag">100% PURE ESSENTIAL OIL</div>
        </div>
        <div class="contact">
          <div class="small">Distributed By:</div>
          <div>Coral Vista, FL 33871</div>
          <div>888-555-KIPO (5476)</div>
          <div>www.volmiraoils.com</div>
        </div>
      </div>
    </section>

    <section class="panel">
      <div class="panel-content front">
        <div class="brand-name">VOLMIRA<sup>™</sup></div>
        <div class="product-box">
          <div class="product-name">LAVENDER</div>
          <div class="latin-name">Lavandula angustifolia</div>
          <div class="purity">100% PURE ESSENTIAL OIL</div>
        </div>
        <div class="net">Net 10ml</div>
      </div>
    </section>

    <section class="panel">
      <div class="panel-frame frame-open-right"></div>
      <div class="panel-content directions">
        <p>Indications: Massage (10 drops of carrier oil for every drop of essential oil), Bath (10 drops of essential oil) or Inhalation (2-4 drops essential of on a tissue).</p>
        <p>Caution: Do not ingest the oil. Sensitive skin may be irritated by topical use. Avoid contact with eyes. Consult your healthcare practitioner before use. Store oil away from children and pets. Not meant for use during pregnancy. Seek medical care immediately if adverse reaction is experienced.</p>
        <p class="warning">EXTERNAL USE ONLY<br>DILUTE BEFORE APPLICATION</p>
      </div>
    </section>
  </div>
</body>
</html>
```